SPICE LABEL DESIGN FOR A TASTY DRY RUB! (chicken, ribs, wings)

Looking for a fun/creative/edgy label for a spice jar! The label will be rectangular (exact size tbd - but approximately 1.2" W X 3" H).
This spice is a dry rub blend of 14 EPIC spices, to be used on chicken, chicken wings, ribs, etc.
Copywritting on the label to be;
Nel DX's Blaze BBQ Rub
A blend of 14 Nel DX Spice Co. spices
*Note the word "unneleivabe" is spelt incorectly on purpose for a play a words with "nel". Please use a different color font for "nel" within the word.
Also would like "Nel DX's" to be prominent
Looking for an illustration/design that is fun/creative/catchy/edgy/appealing! While still keeping the design appealing to higher end markets. Have fun with it and think outside of the box!! :)
People who enjoy cooking, young adults and adults, display at restaurants or retail markets

```html
<!DOCTYPE html>
<html lang="en">
<head>
<meta charset="utf-8">
<title>Nel DX's Blaze BBQ Rub – Chicken Label</title>
<link href="https://fonts.googleapis.com/css2?family=Bitter:wght@700&family=Fira+Sans:wght@700&family=Lobster+Two:ital,wght@1,700&family=Open+Sans:wght@600&family=Poppins:wght@400&display=swap" rel="stylesheet">
<style>
  :root {
    --page: #ffffff;
    --label-black: #0b0b0b;
    --brand-red: #e41e26;
    --ink-white: #ffffff;
    --band-text: #1a1a1a;
    --icon-tone: #f2f2f2;
  }
  * { margin: 0; padding: 0; box-sizing: border-box; }
  html, body {
    width: 1200px;
    height: 907px;
    overflow: hidden;
    background: var(--page);
  }
  .canvas {
    position: relative;
    width: 1200px;
    height: 907px;
  }
  .label {
    position: absolute;
    left: 447px;
    top: 71px;
    width: 305px;
    height: 765px;
    background: var(--label-black);
    color: var(--ink-white);
    overflow: hidden;
  }
  .brand-tab {
    position: absolute;
    left: 46px;
    top: -3px;
    width: 214px;
    height: 143px;
    background: var(--brand-red);
    border: 2px solid var(--ink-white);
    border-top: none;
    border-radius: 0 0 8px 8px;
  }
  .brand-mark {
    position: absolute;
    left: 50%;
    top: 46px;
    width: 22px;
    height: 22px;
    margin-left: -11px;
    border-radius: 50%;
    background: var(--ink-white);
  }
  .brand-name {
    position: absolute;
    left: 0;
    top: 88px;
    width: 100%;
    text-align: center;
    font-family: "Bitter", serif;
    font-weight: 700;
    font-size: 19px;
    line-height: 24px;
    color: var(--ink-white);
  }
  .flavor-icon {
    position: absolute;
    left: 121px;
    top: 232px;
    width: 65px;
    height: 75px;
    border-radius: 8px;
    background: var(--icon-tone);
  }
  .product-title {
    position: absolute;
    left: 0;
    top: 325px;
    width: 100%;
    text-align: center;
    font-family: "Lobster Two", cursive;
    font-style: italic;
    font-weight: 700;
    font-size: 104px;
    line-height: 1;
    letter-spacing: -2px;
  }
  .product-subtitle {
    position: absolute;
    left: 0;
    top: 432px;
    width: 100%;
    text-align: center;
    font-family: "Bitter", serif;
    font-weight: 700;
    font-size: 50px;
    line-height: 1;
    letter-spacing: 4px;
  }
  .product-blurb {
    position: absolute;
    left: 46px;
    top: 496px;
    width: 213px;
    text-align: center;
    font-family: "Open Sans", sans-serif;
    font-weight: 600;
    font-size: 9.5px;
    line-height: 12.5px;
  }
  .flavor-ribbon {
    position: absolute;
    left: 59px;
    top: 613px;
    width: 195px;
    height: 40px;
  }
  .flavor-ribbon svg {
    position: absolute;
    inset: 0;
  }
  .flavor-name {
    position: relative;
    display: block;
    text-align: center;
    font-family: "Fira Sans", sans-serif;
    font-weight: 700;
    font-size: 33px;
    line-height: 40px;
    color: var(--ink-white);
  }
  .product-band {
    position: absolute;
    left: 0;
    top: 697px;
    width: 100%;
    height: 30px;
    background: var(--ink-white);
    color: var(--band-text);
    text-align: center;
    font-family: "Poppins", sans-serif;
    font-size: 13.5px;
    line-height: 30px;
    letter-spacing: 0.6px;
  }
</style>
</head>
<body>
  <main class="canvas">
    <section class="label">
      <div class="brand-tab">
        <span class="brand-mark"></span>
        <span class="brand-name">Nel DX Spice Co.</span>
      </div>

      <div class="flavor-icon" role="img" aria-label="White chicken head icon"></div>

      <h1 class="product-title">BBQ</h1>
      <h2 class="product-subtitle">SPICES</h2>

      <p class="product-blurb">Lorem ipsum dolor sit amet, consectetuer adipiscing elit, sed diam nonummy nibh euismod tincidunt aliquam volutpat.</p>

      <div class="flavor-ribbon">
        <svg viewBox="0 0 195 40" width="195" height="40" aria-hidden="true">
          <polygon points="6,0 195,0 187,20 195,40 0,40 8,20" fill="#e41e26"/>
        </svg>
        <span class="flavor-name">Chicken</span>
      </div>

      <div class="product-band">Nel DX's Blaze BBQ Rub</div>
    </section>
  </main>
</body>
</html>
```